I need the front of this bottle designed for and calendula and tallow lotion. the dimenstions are 236mm by 84 mm the Minimalists design if you choose a graphic should be very minimal and high end I don thave a logo. My company name is The Bright Seed Co, If you want to ceate a logo using the TBSC ( letters only) That would be ok

```html
<!DOCTYPE html>
<html lang="en">
<head>
<meta charset="UTF-8">
<title>The Bright Seed Co — Calendula &amp; Tallow Lotion Label</title>
<link href="https://fonts.googleapis.com/css2?family=Montserrat:wght@400;500;600;700&display=swap" rel="stylesheet">
<style>
  :root {
    --page-bg: #ffffff;
    --kraft: #d8bea9;
    --ink: #2b2420;
    --band-text: #f2e9e1;
    --icon-tone: #b9a08c;
  }
  * { margin: 0; padding: 0; box-sizing: border-box; }
  html, body {
    width: 1200px;
    height: 1200px;
    overflow: hidden;
    background: var(--page-bg);
  }
  .canvas {
    position: relative;
    width: 1200px;
    height: 1200px;
  }
  .label-front {
    position: absolute;
    left: 400px;
    top: 38px;
    width: 400px;
    height: 1124px;
    background: var(--kraft);
    color: var(--ink);
    font-family: 'Montserrat', sans-serif;
    text-align: center;
  }
  .brand-name {
    position: absolute;
    top: 150px;
    left: 0;
    width: 100%;
    font-size: 16px;
    font-weight: 600;
    letter-spacing: 1px;
    line-height: 20px;
  }
  .product-title {
    position: absolute;
    top: 316px;
    left: 0;
    width: 100%;
    font-size: 40px;
    font-weight: 600;
    line-height: 63px;
    letter-spacing: 0.5px;
  }
  .product-type {
    position: absolute;
    top: 555px;
    left: 41px;
    width: 318px;
    height: 49px;
    background: var(--ink);
    color: var(--band-text);
    font-size: 26px;
    font-weight: 500;
    letter-spacing: 8px;
    line-height: 49px;
  }
  .botanical-icon {
    position: absolute;
    top: 695px;
    left: 145px;
    width: 110px;
    height: 158px;
    border-radius: 55px;
    background: var(--icon-tone);
  }
  .net-volume {
    position: absolute;
    top: 1026px;
    left: 0;
    width: 100%;
    font-size: 20px;
    font-weight: 500;
  }
</style>
</head>
<body>
  <main class="canvas">
    <section class="label-front">
      <div class="brand-name">THE BRIGHT SEED CO</div>
      <h1 class="product-title">CALENDULA<br>&amp;<br>TALLOW</h1>
      <div class="product-type">LOTION</div>
      <div class="botanical-icon" role="img" aria-label="Minimal line icon of a calendula flower above an oil droplet"></div>
      <div class="net-volume">net:500ml</div>
    </section>
  </main>
</body>
</html>
```